UX/UI Design of mobile application for language learning through picture cards

We are looking for a Mobile Application Designer with knowledge of UX/UI concepts.

We best candidate is a skilled Mobile Application Designer with knowledge of last trends and with experience in completing similar tasks.

This is a test task. After successful completion, the best candidate will be given a full task.

```html
<!DOCTYPE html>
<html lang="en">
<head>
<meta charset="utf-8">
<title>Picture Cards – Language Learning App Screens</title>
<link rel="stylesheet" href="https://fonts.googleapis.com/css2?family=Inter:wght@400;500;600;700;800&display=swap">
<style>
:root{
  --bg:#d9cdf0;
  --frame:#ffffff;
  --screen:#f2f2f2;
  --ink:#2b2b35;
  --primary:#4a1fa6;
  --primary-deep:#3f0f9e;
  --lilac:#d9cdf3;
  --lilac-text:#7a5cc4;
  --hero-top:#a98fe0;
  --hero-bottom:#6a45c2;
  --ok:#22c27a;
  --bad:#e8303a;
  --link:#0a7fb0;
  --cyan:#7fe3f2;
  --yellow:#f3ef7a;
  --green:#8ef08a;
  --pink:#f07ae0;
}
*{box-sizing:border-box;margin:0;padding:0}
html,body{width:1200px;height:2342px;overflow:hidden;background:var(--bg);font-family:"Inter",sans-serif;color:var(--ink)}
.canvas{position:relative;width:1200px;height:2342px}
.phone{position:absolute;width:522px;height:1101px;background:var(--frame);border-radius:66px;padding:13px;overflow:hidden}
.screen{position:relative;width:100%;height:100%;background:var(--screen);border-radius:54px;overflow:hidden}
.p1{left:70px;top:36px}.p2{left:607px;top:36px}.p3{left:77px;top:1147px}.p4{left:613px;top:1147px}
.abs{position:absolute}
.title{left:57px;top:335px;font-size:40px;font-weight:700;line-height:1.27;letter-spacing:-.5px}
.field{left:53px;top:530px;width:391px;height:79px;background:#fff;border-radius:40px;box-shadow:0 4px 10px rgba(0,0,0,.06);padding:10px 36px}
.field small{display:block;font-size:14px;color:#666}
.field .val{display:flex;align-items:center;gap:10px;font-size:20px;margin-top:6px}
.field svg.chev{position:absolute;right:30px;top:30px}
.btn{display:flex;align-items:center;justify-content:center;gap:10px;color:#fff;background:var(--primary);border-radius:38px;font-weight:700;font-size:23px}
.continue{left:53px;top:891px;width:391px;height:75px;letter-spacing:.3px}
.pill-lang{left:53px;top:60px;width:184px;height:55px;background:#fff;border-radius:28px;box-shadow:0 3px 8px rgba(0,0,0,.07);display:flex;align-items:center;gap:8px;padding-left:24px;font-size:20px}
.pill-lang .edit{width:26px;height:26px;border-radius:50%;background:#eee;display:flex;align-items:center;justify-content:center;margin-left:6px}
.avatar{left:392px;top:94px;width:58px;height:58px;border-radius:50%;background:var(--lilac)}
.hero{left:53px;top:291px;width:391px;height:456px;border-radius:14px;background:linear-gradient(180deg,var(--hero-top),var(--hero-bottom))}
.hero h2{position:absolute;left:36px;top:78px;color:#fff;font-size:42px;font-weight:700;line-height:1.25;letter-spacing:-.5px}
.circ{position:absolute;width:140px;height:140px;border-radius:50%;top:332px;display:flex;align-items:center;justify-content:center}
.upload{left:32px;background:radial-gradient(circle at 40% 40%,#f1fff8,#a9f0d6)}
.camera{left:217px;background:radial-gradient(circle at 40% 40%,#fffaf0,#f5e7b0)}
.photo{left:0;top:0;width:100%;background:linear-gradient(160deg,#5a4a44 0%,#8d7c72 35%,#cfc9c2 65%,#6c6058 100%)}
.sheet{left:0;width:100%;background:#fff;border-radius:54px 54px 0 0}
.sheet3{top:718px;height:400px}
.sheet4{top:579px;height:540px}
.tap{left:0;width:100%;top:778px;text-align:center;font-size:36px;font-weight:600;line-height:1.1;letter-spacing:-.5px}
.max{left:162px;top:933px;width:173px;height:44px;border-radius:22px;background:var(--lilac);color:var(--lilac-text);font-size:20px;font-weight:500;display:flex;align-items:center;justify-content:center}
.box{position:absolute;border:2px solid}
.box .x{position:absolute;right:6px;top:6px;width:16px;height:16px;border-radius:50%;background:#fff;color:#888;font-size:12px;line-height:16px;text-align:center}
.tag{position:absolute;left:0;bottom:0;background:#fff;border-radius:0 8px 0 0;padding:8px 12px 6px 12px;font-size:15px;line-height:1.65}
.tag b{display:block;font-size:14px;font-weight:600;color:#222}
.tag span{display:flex;align-items:center;gap:12px;color:var(--link);font-weight:600;font-size:17px}
.tag i{font-style:normal;font-size:13px;font-weight:800}
.tag .ok{color:var(--ok)}.tag .no{color:var(--bad)}
.detected{left:0;width:100%;top:621px;text-align:center;font-size:36px;font-weight:600;line-height:1.1;letter-spacing:-.5px}
.result{left:54px;width:389px;height:74px;border-radius:37px;background:var(--lilac);display:flex;align-items:center;gap:16px;padding-left:37px;font-size:30px;font-weight:600}
.r1{top:710px}.r2{top:795px}
.load{left:54px;top:955px;width:389px;height:74px;background:var(--primary-deep);font-size:25px;letter-spacing:-.3px}
</style>
</head>
<body>
<div class="canvas">

  <section class="phone p1">
    <div class="screen">
      <h1 class="abs title">Select<br>language to<br>learn</h1>
      <div class="abs field">
        <small>Language</small>
        <div class="val">
          <svg width="28" height="18" viewBox="0 0 28 18"><rect width="28" height="18" fill="#fff"/><g fill="#d22f3c"><rect y="0" width="28" height="2"/><rect y="4" width="28" height="2"/><rect y="8" width="28" height="2"/><rect y="12" width="28" height="2"/><rect y="16" width="28" height="2"/></g><rect width="12" height="10" fill="#3b4a9c"/></svg>
          English (US)
        </div>
        <svg class="chev" width="20" height="12" viewBox="0 0 20 12"><path d="M2 2l8 8 8-8" fill="none" stroke="#333" stroke-width="2"/></svg>
      </div>
      <div class="abs btn continue">CONTINUE
        <svg width="22" height="16" viewBox="0 0 22 16"><path d="M1 8h19M13 1l7 7-7 7" fill="none" stroke="#fff" stroke-width="2.2"/></svg>
      </div>
    </div>
  </section>

  <section class="phone p2">
    <div class="screen">
      <div class="abs pill-lang">
        <svg width="28" height="18" viewBox="0 0 28 18"><rect width="28" height="18" fill="#fff"/><g fill="#d22f3c"><rect y="0" width="28" height="2"/><rect y="4" width="28" height="2"/><rect y="8" width="28" height="2"/><rect y="12" width="28" height="2"/><rect y="16" width="28" height="2"/></g><rect width="12" height="10" fill="#3b4a9c"/></svg>
        EN (US)
        <span class="edit"><svg width="12" height="12" viewBox="0 0 12 12"><path d="M2 10l1-3 5-5 2 2-5 5z" fill="#999"/></svg></span>
      </div>
      <div class="abs avatar"></div>
      <div class="abs hero">
        <h2>Scan or upload<br>a photo to start</h2>
        <div class="circ upload">
          <svg width="84" height="64" viewBox="0 0 84 64"><path d="M42 2l16 18H48v22H36V20H26z" fill="#19c28f"/><path d="M4 40h14v10h48V40h14v22H4z" fill="#19c28f"/></svg>
        </div>
        <div class="circ camera">
          <svg width="86" height="66" viewBox="0 0 86 66"><path d="M6 16h20l6-12h22l6 12h20v46H6z" fill="#ddd3bd"/><circle cx="43" cy="38" r="15" fill="#fffaf0"/><circle cx="43" cy="38" r="9" fill="#ddd3bd"/></svg>
        </div>
      </div>
    </div>
  </section>

  <section class="phone p3">
    <div class="screen">
      <div class="abs photo" style="height:760px" role="img" aria-label="Photo of a man on the phone at a restaurant table with a laptop, notebook and cup"></div>
      <div class="abs sheet sheet3"></div>
      <p class="abs tap">Tap one or more<br>objects to select<br>and continue</p>
      <div class="abs max">5 objects max</div>
    </div>
  </section>

  <section class="phone p4">
    <div class="screen">
      <div class="abs photo" style="height:620px" role="img" aria-label="Same restaurant photo with detected objects highlighted"></div>

      <div class="box" style="left:28px;top:57px;width:184px;height:156px;border-color:var(--cyan)">
        <span class="x">×</span>
        <div class="tag"><b>Select</b><span>Wine <i class="ok">✓</i></span><span>Water</span></div>
      </div>
      <div class="box" style="left:165px;top:196px;width:186px;height:174px;border-color:var(--yellow)">
        <span class="x">×</span>
        <div class="tag"><b>Select</b><span>Head</span><span>Hand <i class="no">×</i></span></div>
      </div>
      <div class="box" style="left:304px;top:357px;width:184px;height:170px;border-color:var(--green)">
        <span class="x">×</span>
        <div class="tag"><b>Select</b><span>Laptop</span><span>Phone <i class="no">×</i></span></div>
      </div>
      <div class="box" style="left:28px;top:423px;width:184px;height:145px;border-color:var(--pink)">
        <span class="x">×</span>
        <div class="tag"><b>Select</b><span>Cup <i class="ok">✓</i></span><span>Tray</span></div>
      </div>

      <div class="abs sheet sheet4"></div>
      <p class="abs detected">4 Objects<br>detected</p>
      <div class="abs result r1">
        <svg width="32" height="32" viewBox="0 0 32 32"><circle cx="16" cy="16" r="16" fill="var(--ok)"/><path d="M9 16l5 5 9-10" fill="none" stroke="#fff" stroke-width="3"/></svg>
        2 Correct answers
      </div>
      <div class="abs result r2">
        <svg width="32" height="32" viewBox="0 0 32 32"><circle cx="16" cy="16" r="16" fill="var(--bad)"/><path d="M11 11l10 10M21 11L11 21" stroke="#fff" stroke-width="3"/></svg>
        2 Inorrect answers
      </div>
      <div class="abs btn load">Load next picture
        <svg width="22" height="16" viewBox="0 0 22 16"><path d="M1 8h19M13 1l7 7-7 7" fill="none" stroke="#fff" stroke-width="2.4"/></svg>
      </div>
    </div>
  </section>

</div>
</body>
</html>
```